Cornflute Firewood advertising Sign for passing by traffic

900mm W
1200mm H

I am looking for a design to place outside of our nursery to advertise our firewood. We have a lot of traffic passing by and want to capture the eyes of potential customers.

We want a modern sleek look that will set the tone for the product

key things i want to hit -
Visual of firewood or fire
Quality product
we deliver
Clean firewood

Target Market(s)

Older retired people
Young families
Passing traffic

Industry/Entity Type

Firewood

Font styles to use
Serif
Sans Serif

Requirements
Must have
• Great eye catching picture
• colorful
• Easy to read for passers by
• Picture of firewood or fireplace or anything you seem relevant to the sale of firewood
• If using picture of firewood make sure it is Australian hardwood
Should not have
• Phone number or business name

```html
<!DOCTYPE html>
<html lang="en">
<head>
<meta charset="utf-8">
<title>Firewood Roadside Sign</title>
<link rel="stylesheet" href="https://fonts.googleapis.com/css2?family=Open+Sans:wght@400;700;800&display=swap">
<style>
  :root {
    --canvas: #e4e6ea;
    --pine: #e6cf9e;
    --pine-light: #f0dfb8;
    --plank-seam: rgba(90, 65, 30, 0.45);
    --ink: #2b2d2e;
    --frame: #2a2b2c;
    --disc: rgba(255, 255, 255, 0.86);
    --white: #ffffff;
  }
  * { box-sizing: border-box; margin: 0; padding: 0; }
  html, body { width: 1200px; height: 1200px; overflow: hidden; }
  body {
    background: var(--canvas);
    font-family: "Open Sans", Arial, sans-serif;
    color: var(--ink);
    position: relative;
  }
  .sign {
    position: absolute;
    left: 246px; top: 36px;
    width: 710px; height: 1106px;
    background:
      repeating-linear-gradient(90deg, transparent 0 122px, var(--plank-seam) 122px 124px),
      linear-gradient(90deg, var(--pine) 0%, var(--pine-light) 50%, var(--pine) 100%);
    overflow: hidden;
  }
  .headline {
    position: absolute; left: 0; right: 0; top: 30px;
    text-align: center; font-weight: 700;
    font-size: 40px; line-height: 62px; letter-spacing: 0.5px;
  }
  .photo {
    position: absolute;
    border: 4px solid var(--frame);
  }
  .photo--split-logs { left: 10px;  top: 209px; width: 334px; height: 337px;
    background: radial-gradient(circle at 40% 40%, #d9a877, #a8774a 60%, #5e3d22); }
  .photo--log-ends   { left: 362px; top: 209px; width: 336px; height: 337px;
    background: radial-gradient(circle at 50% 45%, #e9cfa6, #c69a68 55%, #6b4a2c); }
  .photo--embers     { left: 10px;  top: 562px; width: 334px; height: 334px;
    background: radial-gradient(circle at 50% 75%, #ffb640, #e0561b 45%, #5a1c0e 85%); }
  .photo--flames     { left: 362px; top: 562px; width: 336px; height: 334px;
    background: linear-gradient(100deg, #3a2a22 0%, #b4653a 40%, #f7b65a 70%, #fbe0a0 100%); }
  .badge {
    position: absolute; left: 138px; top: 336px;
    width: 432px; height: 432px; border-radius: 50%;
    background: var(--disc);
    text-align: center;
  }
  .badge__kicker {
    position: absolute; left: 0; right: 0; top: 92px;
    font-weight: 700; font-size: 18px; letter-spacing: 1px;
  }
  .badge__title {
    position: absolute; left: 0; right: 0; top: 142px;
    font-weight: 700; font-size: 58px; line-height: 64px;
  }
  .badge__tag {
    position: absolute; left: 77px; top: 303px;
    width: 278px; height: 44px;
    background: var(--frame);
    transform: skewX(-6deg);
    color: var(--white);
    font-size: 22px; line-height: 44px; letter-spacing: 0.5px;
  }
  .badge__tag span { display: block; transform: skewX(6deg); }
  .delivery {
    position: absolute; left: 0; right: 0; top: 954px;
    text-align: center; font-weight: 700;
  }
  .delivery__label { font-size: 29px; line-height: 40px; }
  .delivery__headline { font-size: 56px; line-height: 70px; font-weight: 800; }
</style>
</head>
<body>
  <main class="sign">
    <h1 class="headline">BEST<br>AUSTRALIAN HARDWOOD</h1>

    <div class="photo photo--split-logs" role="img" aria-label="Stack of split hardwood firewood"></div>
    <div class="photo photo--log-ends" role="img" aria-label="Cut ends of stacked round logs"></div>
    <div class="photo photo--embers" role="img" aria-label="Burning logs over glowing embers"></div>
    <div class="photo photo--flames" role="img" aria-label="Close-up of flames on a burning log"></div>

    <div class="badge">
      <p class="badge__kicker">QUALITY PRODUCT</p>
      <h2 class="badge__title">CLEAN<br>FIREWOOD</h2>
      <p class="badge__tag"><span>SEASONED &amp; SPLIT</span></p>
    </div>

    <footer class="delivery">
      <p class="delivery__label">FAST &amp; FRIENDLY</p>
      <p class="delivery__headline">WE DELIVER</p>
    </footer>
  </main>
</body>
</html>
```